Sudden Tides "Lantern Road" New Single Cover

Create cover artwork for the band Sudden Tides' new single "Lantern Road" being released early 2020. Style, font and graphics to be consistent with band's previous releases and overall brand identity. Visit www.suddentidesband.example and our Spotify page https://music.example.net/artist/7QzWpLx3RtVnKd8e2YbHcJ?si=MUrTgKa4PLe7skvWq2AmZd to view our previous releases and overall brand identity. Some examples attached as well. We are looking for someone to work with on future projects as well.

Lyrics are here: https://docs.example.org/document/d/3KTp9wrn_2ZQa8eXb4Lo_fimH7C5m83Jz4Pd70hrtVcA/edit

Music is here: https://audiostream.example.com/suddentides/lantern-road/s-pzkwa

Font styles to use
Sans Serif

Colors

Designer to choose colors to be used in the design.

Requirements
Must have
• Must be consistent with current brand identity and with prior album / single art.

```html
<!DOCTYPE html>
<html lang="en">
<head>
<meta charset="utf-8">
<title>Sudden Tides – Lantern Road</title>
<link rel="stylesheet" href="https://fonts.googleapis.com/css2?family=Montserrat:wght@300;400&display=swap">
<style>
  :root {
    --brick-light: #f7913f;
    --brick-mid: #f1802f;
    --brick-deep: #e8722a;
    --title-blue: #0ba7ea;
    --band-orange: #e9683a;
  }
  html, body {
    margin: 0;
    padding: 0;
    width: 1200px;
    height: 1198px;
    overflow: hidden;
  }
  .cover {
    position: relative;
    width: 1200px;
    height: 1198px;
    overflow: hidden;
  }
  .cover__wall {
    position: absolute;
    inset: 0;
    background:
      radial-gradient(ellipse at 30% 25%, var(--brick-light) 0%, transparent 60%),
      linear-gradient(160deg, var(--brick-mid) 0%, var(--brick-light) 45%, var(--brick-deep) 100%);
  }
  .cover__type {
    position: absolute;
    inset: 0;
    width: 1200px;
    height: 1198px;
  }
  .title-line {
    font-family: "Montserrat", sans-serif;
    font-weight: 400;
    fill: var(--title-blue);
  }
  .title-line--first { font-size: 326px; }
  .title-line--second { font-size: 438px; }
  .band-name {
    font-family: "Montserrat", sans-serif;
    font-weight: 300;
    font-size: 144px;
    fill: var(--band-orange);
  }
</style>
</head>
<body>
  <main class="cover">
    <div class="cover__wall" role="img" aria-label="Orange-toned photograph of a brick wall filling the whole cover"></div>
    <svg class="cover__type" viewBox="0 0 1200 1198" aria-labelledby="cover-title">
      <title id="cover-title">Lantern Road – Sudden Tides</title>
      <text class="title-line title-line--first" x="68" y="419" textLength="1064" lengthAdjust="spacingAndGlyphs">LANTERN</text>
      <text class="title-line title-line--second" x="68" y="769" textLength="1073" lengthAdjust="spacingAndGlyphs">ROAD</text>
      <text class="band-name" x="68" y="946" textLength="1064" lengthAdjust="spacingAndGlyphs">SUDDEN TIDES</text>
    </svg>
  </main>
</body>
</html>
```